Timber Ridge Land Services Business Cards

Need to create a business card with the company logo "Timber Ridge Land Services". The business will provide forestry mulching for land clearing and vegetation control, brush and small tree removal, wildlife habitat improvement and trail and property access creation.

```html
<!DOCTYPE html>
<html lang="en">
<head>
<meta charset="utf-8">
<title>Timber Ridge Land Services – Business Cards</title>
<link rel="stylesheet" href="https://fonts.googleapis.com/css2?family=Exo+2:ital,wght@0,500;0,700;0,800;1,500;1,700;1,800&display=swap">
<style>
  :root {
    --backdrop: #6f8a86;
    --paper: #ffffff;
    --forest: #0e5a44;
    --leaf: #2f8f4e;
    --sprout: #6cc35f;
    --ink-light: #ffffff;
  }
  * { box-sizing: border-box; margin: 0; padding: 0; }
  html, body {
    width: 1200px; height: 1038px; overflow: hidden;
    background: var(--backdrop);
    font-family: "Exo 2", sans-serif;
  }
  .stage { position: relative; width: 1200px; height: 1038px; }

  .card {
    position: absolute; width: 700px; height: 400px;
    border-radius: 4px; overflow: hidden;
    box-shadow: 0 10px 28px rgba(0,0,0,.28);
  }

  /* Front */
  .card--front { left: 110px; top: 110px; background: var(--paper); }
  .card--front .brand {
    position: absolute; inset: 0;
    display: flex; align-items: center; justify-content: center; gap: 18px;
  }
  .brand__mark { width: 26px; height: 26px; background: var(--leaf); }
  .card--front .brand__name {
    font-weight: 800; font-size: 40px; letter-spacing: .5px;
    color: var(--forest); line-height: 1.05; text-transform: uppercase;
  }

  /* Back */
  .card--back { left: 390px; top: 528px; background: var(--forest); }
  .card--back .glow {
    position: absolute; right: 0; bottom: 0; width: 420px; height: 300px;
    background: radial-gradient(ellipse at 100% 20%, rgba(108,195,95,.28), rgba(108,195,95,0) 70%);
  }
  .card--back .brand {
    position: absolute; right: 34px; top: 36px;
    display: flex; align-items: center; gap: 12px;
  }
  .card--back .brand__mark { width: 14px; height: 14px; background: var(--sprout); }
  .card--back .brand__name {
    font-weight: 800; font-size: 22px; color: var(--ink-light);
    text-transform: uppercase; line-height: 1.05; text-align: right;
  }
  .person { position: absolute; left: 42px; top: 150px; }
  .person__name {
    font-weight: 800; font-style: italic; font-size: 38px; color: var(--sprout);
  }
  .person__role {
    font-weight: 500; font-style: italic; font-size: 20px; color: var(--leaf);
    margin-top: -4px;
  }
  .contacts { position: absolute; left: 42px; top: 256px; list-style: none; }
  .contacts li {
    display: flex; align-items: flex-start; gap: 14px;
    color: var(--ink-light); font-weight: 700; font-style: italic;
    font-size: 17px; line-height: 1.3; margin-bottom: 8px;
  }
  .contacts li.contacts__phone { font-size: 26px; align-items: center; }
  .contacts svg { width: 16px; height: 16px; flex: none; margin-top: 3px; }
  .contacts__phone svg { margin-top: 0; }
  .website {
    position: absolute; right: 34px; bottom: 38px;
    color: var(--sprout); font-weight: 700; font-style: italic; font-size: 20px;
  }
</style>
</head>
<body>
<main class="stage">
  <section class="card card--front" aria-label="Card front">
    <div class="brand">
      <span class="brand__mark"></span>
      <span class="brand__name">Timber Ridge<br>Land Services</span>
    </div>
  </section>

  <section class="card card--back" aria-label="Card back">
    <div class="glow" role="img" aria-label="Soft green decorative accent"></div>

    <div class="brand">
      <span class="brand__mark"></span>
      <span class="brand__name">Timber Ridge<br>Land Services</span>
    </div>

    <div class="person">
      <p class="person__name">Daniel Reyes</p>
      <p class="person__role">Manager</p>
    </div>

    <ul class="contacts">
      <li class="contacts__phone">
        <svg viewBox="0 0 16 16" fill="#6cc35f"><path d="M3 1h3l1.5 4-2 1.3a9 9 0 0 0 4.2 4.2L11 8.5l4 1.5v3a2 2 0 0 1-2 2A12 12 0 0 1 1 3a2 2 0 0 1 2-2z"/></svg>
        555-014-2287
      </li>
      <li>
        <svg viewBox="0 0 16 16" fill="none" stroke="#6cc35f" stroke-width="1.6"><rect x="1.5" y="3.5" width="13" height="9"/><path d="M1.5 3.5 8 9l6.5-5.5"/></svg>
        info@timberridgeland.com
      </li>
      <li>
        <svg viewBox="0 0 16 16" fill="#6cc35f"><path d="M8 1a5 5 0 0 1 5 5c0 4-5 9-5 9S3 10 3 6a5 5 0 0 1 5-5zm0 3a2 2 0 1 0 0 4 2 2 0 0 0 0-4z"/></svg>
        <span>42 Quarry Lane, Unit 7<br># 48210</span>
      </li>
    </ul>

    <p class="website">timberridgeland.com</p>
  </section>
</main>
</body>
</html>
```